Journeys With Marlowe Business Cards

I need a business card design for my upscale Travel Agency.
Attached you can find my logo.
I would like to include the following:
- Name
- Title
- Phone Number
- Email
- Website
- and then something like: Follow us: JourneysWithMarlowe (and then social media icons in color).
The logo should be in the front and then also the back.
I am also attaching a design that I liked (mostly for the layout) but open to any suggestions
Industry/Entity Type
Travel Agent
Contact Information for Business Card
Name: Celine Drummond
Title: Travel Designer / Owner
Phone: 415-296-0487
Email: celine@journeyswithmarlowe.example
Website: www.JourneysWithMarlowe.example
Social Media Handles for FB,IG, Twitter: JourneysWithMarlowe
Font styles to use
Colors
Designer to choose colors to be used in the design.
Look and feel

```html
<!DOCTYPE html>
<html lang="en">
<head>
<meta charset="utf-8">
<title>Journeys With Marlowe – Business Cards</title>
<link href="https://fonts.googleapis.com/css2?family=Roboto:wght@400;500;700&display=swap" rel="stylesheet">
<style>
  :root {
    --backdrop: #808080;
    --card: #ffffff;
    --accent: #f2a65a;
    --accent-deep: #d9823a;
    --accent-soft: #f7c48f;
    --ink: #1f1f1f;
  }
  * { box-sizing: border-box; margin: 0; padding: 0; }
  html, body { width: 1200px; height: 1020px; overflow: hidden; }
  body {
    background: var(--backdrop);
    font-family: "Roboto", Arial, sans-serif;
    color: var(--ink);
    position: relative;
  }
  .card {
    position: absolute;
    width: 656px;
    height: 375px;
    background: var(--card);
    border-radius: 20px;
  }
  .card--front { left: 272px; top: 88px; }
  .card--back { left: 271px; top: 514px; }

  .brand {
    position: absolute;
    display: flex;
    align-items: center;
    color: var(--accent);
    font-weight: 500;
    white-space: nowrap;
  }
  .brand__square { background: var(--accent); flex: none; }
  .card--front .brand { left: 40px; top: 174px; font-size: 20px; gap: 10px; }
  .card--front .brand__square { width: 18px; height: 18px; }
  .card--back .brand { left: 104px; top: 160px; font-size: 36px; gap: 16px; }
  .card--back .brand__square { width: 34px; height: 34px; }

  .divider {
    position: absolute;
    left: 308px;
    width: 2px;
    background: var(--accent);
  }
  .divider--name { top: 110px; height: 40px; }
  .divider--contact { top: 172px; height: 112px; }

  .person { position: absolute; left: 326px; top: 104px; white-space: nowrap; }
  .person__name { color: var(--accent); font-weight: 700; font-size: 23px; line-height: 30px; }
  .person__title { font-size: 17px; line-height: 22px; }

  .contact { position: absolute; left: 326px; top: 170px; list-style: none; }
  .contact__item {
    display: flex;
    align-items: center;
    height: 25px;
    font-size: 15.5px;
    white-space: nowrap;
  }
  .contact__icon { width: 16px; height: 16px; margin-right: 12px; flex: none; }

  .follow {
    position: absolute;
    left: 326px;
    top: 262px;
    display: flex;
    align-items: center;
    font-size: 14px;
    white-space: nowrap;
  }
  .follow__label { color: var(--accent); font-weight: 500; margin-right: 5px; }
  .follow__icons { display: flex; gap: 6px; margin-left: 10px; }
  .follow__icon { width: 16px; height: 16px; border-radius: 50%; }
  .follow__icon--one { background: var(--accent-deep); }
  .follow__icon--two { background: var(--accent); }
  .follow__icon--three { background: var(--accent-soft); }

  .site {
    position: absolute;
    left: 0; right: 0;
    top: 326px;
    text-align: center;
    font-size: 17.5px;
    letter-spacing: 2px;
  }
  .site__name { color: var(--accent); }
</style>
</head>
<body>
  <section class="card card--front">
    <div class="brand"><span class="brand__square"></span>Journeys With Marlowe</div>

    <span class="divider divider--name"></span>
    <div class="person">
      <p class="person__name">Celine Drummond</p>
      <p class="person__title">Travel Designer / Owner</p>
    </div>

    <span class="divider divider--contact"></span>
    <ul class="contact">
      <li class="contact__item">
        <svg class="contact__icon" viewBox="0 0 16 16" fill="#f2a65a"><path d="M3.5 1.5l2.5 0 1 3.5-1.6 1.3c.8 1.7 2.1 3 3.8 3.8l1.3-1.6 3.5 1v2.5c0 .8-.7 1.5-1.5 1.5C7 13.5 2 8.5 2 3c0-.8.7-1.5 1.5-1.5z"/></svg>
        415-296-0487
      </li>
      <li class="contact__item">
        <svg class="contact__icon" viewBox="0 0 16 16" fill="#f2a65a"><path d="M1 3.5h14v9H1z"/><path d="M1.5 4l6.5 5 6.5-5" fill="none" stroke="#fff" stroke-width="1.2"/></svg>
        celine@journeyswithmarlowe.example
      </li>
      <li class="contact__item">
        <svg class="contact__icon" viewBox="0 0 16 16" fill="none"><circle cx="8" cy="8" r="6.5" fill="#f2a65a"/><ellipse cx="8" cy="8" rx="2.8" ry="6.5" stroke="#fff" stroke-width="1"/><line x1="1.5" y1="8" x2="14.5" y2="8" stroke="#fff" stroke-width="1"/></svg>
        www.JourneysWithMarlowe.example
      </li>
    </ul>
    <div class="follow">
      <span class="follow__label">Follow us:</span>JourneysWithMarlowe
      <span class="follow__icons" role="img" aria-label="Social media icons">
        <span class="follow__icon follow__icon--one"></span>
        <span class="follow__icon follow__icon--two"></span>
        <span class="follow__icon follow__icon--three"></span>
      </span>
    </div>
  </section>

  <section class="card card--back">
    <div class="brand"><span class="brand__square"></span>Journeys With Marlowe</div>
    <p class="site">www.<span class="site__name">JourneysWithMarlowe</span>.example</p>
  </section>
</body>
</html>
```